Web design project for exciting Australian start-up

Background
We are looking for a creative and talented web design artist to work alongside our market leading web developer.
• You will be required to create a modern and clean design theme for our website, incorporating selected rustic colour scheme elements for our exciting Australian start-up to operate within the coffee industry.
reoccurring work to be expected to flow to the successful designer.
Requirements
• c. 5 - 10 page website
• Landing page
• Log in/ out
• 404 template
• Typography is emphasised
• Please use either a) typevane.com, b) free web fonts, c) marlo fonts
• All design elements in vector format
• Preferably with icons for each header title(i.e. about us, how it works etc) but designer have free reign over how the site looks, so might not be applicable
• All pages to be responsive
• Down to iPad resolution

High level visual design brief attached - additional pages to be worked from base design.

Design inspiration
• We would like to use design elements from the following sources:
http://www.brivantel.com/sorvik/ (Functionality)
Colour scheme refer to logo and complementary style guide
Updates

```html
<!DOCTYPE html>
<html lang="en">
<head>
<meta charset="utf-8">
<title>Roastwell – Marketplace</title>
<link rel="stylesheet" href="https://fonts.googleapis.com/css2?family=Open+Sans:wght@400;600;700;800&display=swap">
<style>
:root{
  --orange:#f0962a;
  --orange-soft:#e2a557;
  --ink:#222;
  --text:#444;
  --muted:#666;
  --line:#dcdcdc;
  --panel:#f6f6f6;
  --cream:#fbecd5;
  --cream-deep:#f7e2c2;
  --black:#111;
  --grey-star:#cfcfcf;
}
*{box-sizing:border-box;margin:0;padding:0}
html,body{width:1174px;height:1200px;overflow:hidden}
body{position:relative;background:#fff;font-family:"Open Sans",Arial,sans-serif;color:var(--text)}
.abs{position:absolute}
.scallop{top:0;left:0;width:1174px;height:12px}
.header{top:0;left:0;width:1174px;height:141px;border-bottom:1px solid #e6e6e6;background:linear-gradient(#fff 60%,#f7f7f7)}
.brand{top:29px;left:98px;height:94px;display:flex;align-items:center;gap:14px}
.brand-mark{width:86px;height:86px;border-radius:50%;background:var(--orange-soft);border:4px solid var(--black)}
.brand-name{font-weight:800;font-size:36px;letter-spacing:2px;color:var(--black)}
.btn{display:flex;align-items:center;justify-content:center;font-size:14px;border-radius:2px}
.btn-account{top:64px;left:817px;width:108px;height:36px;background:var(--orange);color:#fff;font-weight:600}
.btn-login{top:64px;left:933px;width:146px;height:36px;background:var(--black);color:#fff;font-weight:600;font-size:13px}
.page-title{top:172px;left:98px;font-size:32px;color:var(--orange);font-weight:400}
.filter{top:233px;height:33px;border:1px solid #ccc;background:linear-gradient(#fff,#f1f1f1);color:var(--muted);font-size:14px}
.filter.is-active{background:var(--orange);border-color:var(--orange);color:#fff}
.filter.is-bold{font-weight:600}
.searchbar{top:291px;left:98px;width:983px;height:43px;border:1px solid var(--line);background:var(--panel);font-size:14px;color:var(--muted)}
.searchbar .item{position:absolute;top:0;height:41px;display:flex;align-items:center;gap:6px}
.select{height:31px;border:1px solid var(--line);background:#fff;display:flex;align-items:center;justify-content:space-between;padding:0 9px;font-size:13px}
.results-title{top:349px;left:98px;font-size:27px;color:var(--ink)}
.results{top:395px;left:98px;width:985px;height:443px;border:1px solid var(--line)}
.row{position:absolute;left:0;width:983px;height:148px;background:linear-gradient(#fff 70%,#f3f3f3);border-bottom:1px solid var(--line)}
.row:last-child{border-bottom:none}
.roaster{position:absolute;left:14px;top:40px;width:130px;height:64px;display:flex;flex-direction:column;align-items:center;justify-content:center;gap:6px}
.roaster .dot{width:18px;height:18px;border-radius:50%;background:var(--orange-soft)}
.roaster .name{font-size:17px;font-weight:600;color:#5a3722}
.bean-title{position:absolute;left:154px;top:18px;font-size:19px;color:var(--orange)}
.bean-info{position:absolute;left:155px;top:47px;width:540px;font-size:12.5px;line-height:17px;color:var(--muted)}
.bean-info b{font-weight:400;color:var(--ink)}
.bean-info p+p{margin-top:7px}
.divider{position:absolute;left:676px;top:16px;width:1px;height:116px;background:var(--line)}
.bubble{position:absolute;left:703px;top:20px}
.review-title{position:absolute;left:758px;top:18px;font-size:19px;color:var(--orange)}
.stars{position:absolute;left:758px;top:46px;display:flex;gap:2px}
.rating-note{position:absolute;right:22px;top:71px;text-align:right;font-size:11.5px;line-height:17px;color:var(--muted)}
.icons{position:absolute;left:710px;top:99px;display:flex;gap:6px}
.offerings{position:absolute;right:22px;top:111px;font-size:12.5px;font-weight:600;color:var(--ink)}
.footer{top:890px;left:0;width:1174px;height:252px;background:linear-gradient(var(--cream),#fdf3e3)}
.footer-bar{top:1142px;left:0;width:1174px;height:58px;background:#fdf6ec;border-top:1px solid #f1e1c8}
.tab{position:absolute;top:35px;width:232px;height:37px;background:var(--orange);color:#fff;font-size:18px;padding-left:22px;display:flex;align-items:center;clip-path:polygon(0 0,216px 0,100% 50%,216px 100%,0 100%)}
.links{position:absolute;top:93px;list-style:none;font-size:13px;color:var(--text)}
.links li{height:27px;display:flex;align-items:center;gap:8px}
.social-dot{width:18px;height:18px;background:var(--muted);border-radius:2px}
.copyright{top:1165px;left:110px;font-size:12px;color:var(--orange)}
</style>
</head>
<body>

<svg class="abs scallop" viewBox="0 0 1174 12" preserveAspectRatio="none">
  <defs>
    <pattern id="scallops" width="20" height="12" patternUnits="userSpaceOnUse">
      <path d="M0 0H20V4A10 8 0 0 1 0 4Z" fill="#e2a557"/>
    </pattern>
  </defs>
  <rect width="1174" height="12" fill="url(#scallops)"/>
</svg>

<header class="abs header">
  <div class="abs brand">
    <div class="brand-mark"></div>
    <span class="brand-name">ROASTWELL</span>
  </div>
  <div class="abs btn btn-account">My Account</div>
  <div class="abs btn btn-login">LOGIN IN&nbsp;&nbsp;|&nbsp;&nbsp;LOGOUT</div>
</header>

<h1 class="abs page-title">Marketplace</h1>

<div class="abs btn filter" style="left:99px;width:137px">Tender Format</div>
<div class="abs btn filter is-active" style="left:245px;width:60px">All</div>
<div class="abs btn filter" style="left:314px;width:85px">One-off</div>
<div class="abs btn filter" style="left:409px;width:100px">Recurring</div>
<div class="abs btn filter" style="left:855px;width:110px">Quantity (kg)</div>
<div class="abs btn filter is-active is-bold" style="left:974px;width:107px">35 kg/week</div>

<div class="abs searchbar">
  <div class="item" style="left:15px"><span style="font-weight:600">[X]</span> Results for Cafe Marrow</div>
  <div class="item" style="left:226px">
    <svg width="18" height="18" viewBox="0 0 24 24"><path d="M12 2l3 7 7 .6-5.3 4.7 1.6 7.2L12 17.8 5.7 21.5l1.6-7.2L2 9.6 9 9z" fill="#f0962a"/></svg>
    Save Search
  </div>
  <div class="item" style="left:724px;font-size:13px">Sort</div>
  <div class="item" style="left:758px"><div class="select" style="width:116px">Highest rated
    <svg width="10" height="6" viewBox="0 0 10 6"><path d="M0 0h10L5 6z" fill="#555"/></svg></div></div>
  <div class="item" style="left:889px;font-size:13px">View</div>
  <div class="item" style="left:917px"><div class="select" style="width:55px">
    <svg width="22" height="18" viewBox="0 0 22 18"><rect x="0" y="0" width="10" height="8" rx="3" fill="#f0962a"/><rect x="12" y="0" width="10" height="8" rx="3" fill="#f0962a"/><rect x="0" y="10" width="10" height="8" rx="3" fill="#f0962a"/><rect x="12" y="10" width="10" height="8" rx="3" fill="#f0962a"/></svg>
    <svg width="10" height="6" viewBox="0 0 10 6"><path d="M0 0h10L5 6z" fill="#555"/></svg></div></div>
</div>

<h2 class="abs results-title" style="font-weight:400">Results</h2>

<svg width="0" height="0" style="position:absolute">
  <defs>
    <symbol id="star" viewBox="0 0 24 24"><path d="M12 2l3 7 7 .6-5.3 4.7 1.6 7.2L12 17.8 5.7 21.5l1.6-7.2L2 9.6 9 9z"/></symbol>
    <symbol id="ico-cert" viewBox="0 0 26 24"><path d="M1 1h22v22H1z" fill="none" stroke="#111" stroke-width="3"/><rect x="6" y="7" width="13" height="10" fill="#111"/><path d="M19 12h6" stroke="#111" stroke-width="3"/></symbol>
    <symbol id="ico-cap" viewBox="0 0 36 24"><path d="M1 9L18 2l17 7-17 7z" fill="#111"/><path d="M8 13v6c5 4 15 4 20 0v-6l-10 4z" fill="#111"/><rect x="32" y="10" width="2" height="11" fill="#111"/></symbol>
    <symbol id="ico-cup" viewBox="0 0 20 24"><path d="M1 1h18l-3 22H4z" fill="#111"/><rect x="6" y="6" width="8" height="7" fill="#fff"/></symbol>
    <symbol id="ico-horn" viewBox="0 0 30 24"><path d="M2 8h8l14-7v22L10 16H2z" fill="#111"/><rect x="6" y="16" width="5" height="7" fill="#111"/><rect x="25" y="9" width="4" height="6" fill="#111"/></symbol>
  </defs>
</svg>

<section class="abs results">
  <article class="row" style="top:0">
    <div class="roaster"><span class="dot"></span><span class="name">Larkspur</span></div>
    <h3 class="bean-title" style="font-weight:400">Coffee Bean</h3>
    <div class="bean-info">
      <p><b>Blend Description:</b> Morbi diam mauris viverra in gravida eu mattis in ante Morbi eget arcu Morbi porta libero id ullamcorper nonummy nibh ligula pulvinar metus</p>
      <p><b>Origin:</b> 15285</p>
      <p><b>Grind availability:</b> 15285</p>
    </div>
    <div class="divider"></div>
    <svg class="bubble" width="48" height="34" viewBox="0 0 48 34"><ellipse cx="24" cy="14" rx="23" ry="13" fill="#e2a557"/><path d="M10 23l-3 10 12-8z" fill="#e2a557"/></svg>
    <h4 class="review-title" style="font-weight:400">Reviews for this bean</h4>
    <div class="stars">
      <svg width="16" height="16" fill="#f0962a"><use href="#star"/></svg><svg width="16" height="16" fill="#f0962a"><use href="#star"/></svg><svg width="16" height="16" fill="#f0962a"><use href="#star"/></svg><svg width="16" height="16" fill="#cfcfcf"><use href="#star"/></svg><svg width="16" height="16" fill="#cfcfcf"><use href="#star"/></svg>
    </div>
    <div class="rating-note">Wholesaler's overall<br>Customer rating</div>
    <div class="icons">
      <svg width="26" height="24"><use href="#ico-cert"/></svg><svg width="36" height="24"><use href="#ico-cap"/></svg><svg width="20" height="24"><use href="#ico-cup"/></svg><svg width="30" height="24"><use href="#ico-horn"/></svg>
    </div>
    <div class="offerings">Other offerings</div>
  </article>

  <article class="row" style="top:148px">
    <div class="roaster"><span class="dot" style="background:#7bb23c"></span><span class="name">Verdant Roast</span></div>
    <h3 class="bean-title" style="font-weight:400">Coffee Bean</h3>
    <div class="bean-info">
      <p><b>Blend Description:</b> Morbi diam mauris viverra in gravida eu mattis in ante Morbi eget arcu Morbi porta libero id ullamcorper nonummy nibh ligula pulvinar metus</p>
      <p><b>Origin:</b> 15285</p>
      <p><b>Grind availability:</b> 15285</p>
    </div>
    <div class="divider"></div>
    <svg class="bubble" width="48" height="34" viewBox="0 0 48 34"><ellipse cx="24" cy="14" rx="23" ry="13" fill="#e2a557"/><path d="M10 23l-3 10 12-8z" fill="#e2a557"/></svg>
    <h4 class="review-title" style="font-weight:400">Reviews for this bean</h4>
    <div class="stars">
      <svg width="16" height="16" fill="#f0962a"><use href="#star"/></svg><svg width="16" height="16" fill="#f0962a"><use href="#star"/></svg><svg width="16" height="16" fill="#f0962a"><use href="#star"/></svg><svg width="16" height="16" fill="#cfcfcf"><use href="#star"/></svg><svg width="16" height="16" fill="#cfcfcf"><use href="#star"/></svg>
    </div>
    <div class="rating-note">Wholesaler's overall<br>Customer rating</div>
    <div class="icons">
      <svg width="26" height="24"><use href="#ico-cert"/></svg><svg width="36" height="24"><use href="#ico-cap"/></svg><svg width="20" height="24"><use href="#ico-cup"/></svg><svg width="30" height="24"><use href="#ico-horn"/></svg>
    </div>
    <div class="offerings">Other offerings</div>
  </article>

  <article class="row" style="top:296px">
    <div class="roaster"><span class="dot" style="background:#333"></span><span class="name" style="color:#222">Tamsin &amp; Co</span></div>
    <h3 class="bean-title" style="font-weight:400">Coffee Bean</h3>
    <div class="bean-info">
      <p><b>Blend Description:</b> Morbi diam mauris viverra in gravida eu mattis in ante Morbi eget arcu Morbi porta libero id ullamcorper nonummy nibh ligula pulvinar metus</p>
      <p><b>Origin:</b> 15285</p>
      <p><b>Grind availability:</b> 15285</p>
    </div>
    <div class="divider"></div>
    <svg class="bubble" width="48" height="34" viewBox="0 0 48 34"><ellipse cx="24" cy="14" rx="23" ry="13" fill="#e2a557"/><path d="M10 23l-3 10 12-8z" fill="#e2a557"/></svg>
    <h4 class="review-title" style="font-weight:400">Reviews for this bean</h4>
    <div class="stars">
      <svg width="16" height="16" fill="#f0962a"><use href="#star"/></svg><svg width="16" height="16" fill="#f0962a"><use href="#star"/></svg><svg width="16" height="16" fill="#f0962a"><use href="#star"/></svg><svg width="16" height="16" fill="#cfcfcf"><use href="#star"/></svg><svg width="16" height="16" fill="#cfcfcf"><use href="#star"/></svg>
    </div>
    <div class="rating-note">Wholesaler's overall<br>Customer rating</div>
    <div class="icons">
      <svg width="26" height="24"><use href="#ico-cert"/></svg><svg width="36" height="24"><use href="#ico-cap"/></svg><svg width="20" height="24"><use href="#ico-cup"/></svg><svg width="30" height="24"><use href="#ico-horn"/></svg>
    </div>
    <div class="offerings">Other offerings</div>
  </article>
</section>

<footer class="abs footer">
  <div class="tab" style="left:99px">Helpful Information</div>
  <div class="tab" style="left:357px">Who we are</div>
  <div class="tab" style="left:620px">Join Us Now</div>
  <ul class="links" style="left:121px">
    <li>About us</li><li>Media enquiries</li><li>Terms &amp; conditions</li><li>Privacy policy</li>
  </ul>
  <ul class="links" style="left:376px">
    <li>How it works</li><li>FAQ</li><li>Contact us</li>
  </ul>
  <ul class="links" style="left:642px">
    <li><span class="social-dot"></span>Friendlane</li>
    <li><span class="social-dot"></span>Chirpline</li>
    <li><span class="social-dot"></span>Workweave</li>
    <li><span class="social-dot"></span>Clipstream</li>
  </ul>
</footer>
<div class="abs footer-bar"></div>
<p class="abs copyright">© 2014 Company Name&nbsp; All right reserved&nbsp; Term of Use</p>

</body>
</html>
```